Stationary For Accounting Firm
TALLORAN BREVIK PC
Professional
Jaspal T Varikh
Principal
482 W Orchard Ln Hightstown, NJ 08377
jvarikh@talloranbrevik.com
www.talloranbrevik.com
Only use my name, title, and email address on business card.

```html
<!DOCTYPE html>
<html lang="en">
<head>
<meta charset="utf-8">
<title>Talloran Brevik PC – Business Card</title>
<link rel="stylesheet" href="https://fonts.googleapis.com/css2?family=Raleway:wght@300;400;500&display=swap">
<style>
  :root {
    --card-grey: #d6d6d7;
    --brand-blue: #1f78bf;
    --name-blue: #2a80c4;
    --ink-grey: #5b5b5d;
    --title-grey: #3f3f41;
    --band-dark: #4b4b4d;
    --white: #ffffff;
  }
  html, body {
    margin: 0;
    padding: 0;
    width: 1200px;
    height: 686px;
    overflow: hidden;
    background: var(--card-grey);
  }
  .card {
    position: relative;
    width: 1200px;
    height: 686px;
    background: var(--card-grey);
    font-family: "Raleway", sans-serif;
    overflow: hidden;
  }
  .brand-mark {
    position: absolute;
    left: 420px;
    top: 149px;
    width: 360px;
    height: 242px;
    background: var(--brand-blue);
  }
  .firm {
    position: absolute;
    left: 40px;
    top: 440px;
    width: 530px;
  }
  .firm-name {
    margin: 0;
    font-weight: 300;
    font-size: 76px;
    line-height: 1;
    color: var(--ink-grey);
    white-space: nowrap;
    letter-spacing: -0.5px;
  }
  .firm-rule {
    display: flex;
    align-items: center;
    gap: 10px;
    margin-top: 12px;
    color: var(--ink-grey);
    font-size: 15px;
    font-weight: 400;
    letter-spacing: 1px;
  }
  .firm-rule::before,
  .firm-rule::after {
    content: "";
    flex: 1;
    height: 1.5px;
    background: var(--ink-grey);
  }
  .firm-services {
    margin: 8px 0 0;
    text-align: center;
    font-size: 17px;
    font-weight: 400;
    letter-spacing: 7px;
    color: var(--ink-grey);
    white-space: nowrap;
  }
  .person {
    position: absolute;
    right: 77px;
    top: 468px;
    text-align: right;
  }
  .person-name {
    margin: 0;
    font-size: 37px;
    font-weight: 400;
    color: var(--name-blue);
    line-height: 1.2;
  }
  .person-title {
    margin: 8px 0 0;
    font-size: 35px;
    font-weight: 400;
    color: var(--title-grey);
    line-height: 1.2;
  }
  .bottom-bands {
    position: absolute;
    left: 0;
    top: 600px;
    width: 1200px;
    height: 86px;
  }
  .email {
    position: absolute;
    right: 22px;
    top: 614px;
    margin: 0;
    font-size: 36px;
    font-weight: 400;
    color: var(--white);
    line-height: 1.2;
  }
</style>
</head>
<body>
  <main class="card">
    <div class="brand-mark" aria-hidden="true"></div>

    <section class="firm">
      <h1 class="firm-name">Talloran Brevik</h1>
      <div class="firm-rule">PC</div>
      <p class="firm-services">ACCOUNTING | TAX | ADVISORY</p>
    </section>

    <section class="person">
      <p class="person-name">Jaspal T Varikh</p>
      <p class="person-title">Principal</p>
    </section>

    <svg class="bottom-bands" viewBox="0 0 1200 86" aria-hidden="true">
      <rect x="0" y="0" width="560" height="86" fill="var(--brand-blue)"/>
      <polygon points="468,0 1200,0 1200,86 510,86" fill="var(--band-dark)"/>
    </svg>

    <p class="email">jvarikh@talloranbrevik.com</p>
  </main>
</body>
</html>
```